Feature film needs look book digital brochure - Media/Investor's package

Looking for a designer to create an edgy, eye popping visual representation of my film to get interest from investors, producers and actors, along with Investor and Sponsorship information. Basically it would introduce the project and in about 9-13 pages; give an overview of the film, why to invest, an artistic statement and potential casting ideas and an introduction to the key crew. I have included images (probably more than you need), our film's key art (harbor glass final image & bib logo), and our company (Corvane)'s logo. I've also included samples for another film (tqwl_proposal.pdf) and a proposal I already did for the film. The sample for the other film is more visual and something I'd like to emulate.

The film is called Harbor Glass: a sports drama about two triathletes who overcome their personal demons to train for and compete in the biggest race of their lives.

```html
<!DOCTYPE html>
<html lang="en">
<head>
<meta charset="utf-8">
<title>Harbor Glass – Sources of Revenue &amp; Distribution</title>
<link href="https://fonts.googleapis.com/css2?family=Carlito:wght@400;700&display=swap" rel="stylesheet">
<style>
  :root {
    --ink: #111111;
    --accent: #d4891c;
    --rule: #e08a2a;
    --header-fill: #c8d2cb;
    --sage: #b9c6bf;
    --sage-soft: #dfe6e1;
    --brand-faint: rgba(150,165,158,0.45);
    --paper: #ffffff;
  }
  html, body { margin: 0; padding: 0; overflow: hidden; }
  body {
    width: 1200px; height: 1000px; position: relative;
    background: var(--paper);
    font-family: "Carlito", "Calibri", Arial, sans-serif;
    color: var(--ink);
  }
  .page {
    position: absolute; left: 203px; top: 193px;
    width: 792px; height: 611px;
    border: 1px solid #000; overflow: hidden;
    background: var(--paper);
  }
  .brand-backdrop {
    position: absolute; left: 330px; top: 0; width: 462px; height: 611px;
    background: linear-gradient(90deg, rgba(255,255,255,1) 0%, rgba(223,230,225,0.7) 30%, var(--sage-soft) 100%);
  }
  .brand-figure {
    position: absolute; left: 400px; top: 20px; width: 390px; height: 420px;
    border-radius: 50% 50% 40% 40%;
    background: radial-gradient(ellipse at 50% 45%, rgba(185,198,191,0.75), rgba(185,198,191,0) 70%);
  }
  .brand-name {
    position: absolute; left: 440px; top: 470px; margin: 0;
    font-size: 80px; font-weight: 400; line-height: 1;
    color: var(--brand-faint); white-space: nowrap;
  }
  .title {
    position: absolute; left: 18px; top: 20px; margin: 0;
    font-size: 21px; font-weight: 400; letter-spacing: 3.3px;
    color: var(--accent); white-space: nowrap;
  }
  .title-rule {
    position: absolute; left: 0; top: 52px; width: 520px; height: 1px;
    background: linear-gradient(90deg, var(--rule) 70%, rgba(224,138,42,0));
  }
  .intro {
    position: absolute; left: 22px; top: 70px; width: 385px; margin: 0;
    font-size: 11px; font-weight: 700; line-height: 14.5px;
  }
  .windows {
    position: absolute; left: 22px; top: 174px;
    border-collapse: collapse; table-layout: fixed; width: 380px;
    background: var(--paper);
  }
  .windows col { width: 95px; }
  .windows th, .windows td {
    border: 1px solid var(--rule);
    text-align: center; vertical-align: middle;
    font-size: 7px; font-weight: 700; line-height: 9px; padding: 0 4px;
    overflow: hidden;
  }
  .windows th {
    background: var(--header-fill); height: 27px;
    font-size: 9px; line-height: 10px;
  }
  .windows tr.r1 td { height: 50px; }
  .windows tr.r2 td { height: 49px; }
  .windows tr.r3 td { height: 61px; }
  .windows tr.r4 td { height: 49px; }
  .windows tr.r5 td { height: 49px; }
  .windows tr.r6 td { height: 48px; }
  .windows tr.r7 td { height: 48px; }
  .page-number {
    position: absolute; left: 760px; top: 588px; width: 16px; height: 16px;
    border: 1px solid #fff; border-radius: 50%;
    color: #fff; font-size: 10px; line-height: 16px; text-align: center;
  }
</style>
</head>
<body>
  <section class="page">
    <div class="brand-backdrop"></div>
    <div class="brand-figure" role="img" aria-label="Faint company emblem artwork"></div>
    <p class="brand-name">Corvane</p>

    <h1 class="title">Harbor Glass: Sources of Revenue &amp; Distribution Information</h1>
    <div class="title-rule"></div>

    <p class="intro">After a 4-6 month theatrical run, we will sell DVD's through our website, Parcelry and other fulfillment companies, and self-release through the VOD windows like Reelio rental and sales and approach a distributor like Relaybrook to gain access to the Cable VOD market, Tunebox, Lumo, Flickstream and big box retail stores. Here is our proposed platform window:</p>

    <table class="windows">
      <colgroup><col><col><col><col></colgroup>
      <thead>
        <tr>
          <th>Platform</th>
          <th>Months After Initial Theatrical Release</th>
          <th>Estimated Length of Time</th>
          <th>Conversion</th>
        </tr>
      </thead>
      <tbody>
        <tr class="r1">
          <td>Domestic Theatrical on Demand through Rallyhouse/ Verity/Screenwell (30-50 theatrical dates in North America</td>
          <td>--</td>
          <td>4 - 6 Months</td>
          <td>3000 -5000 ticketed attendance. Goal: Publicity, break even</td>
        </tr>
        <tr class="r2">
          <td>Domestic Home Video (initial) - DVD/Blue Ray sales</td>
          <td>3 - 6 Months</td>
          <td>6 - 12 Months</td>
          <td>10,000 DVDs at $15 each, 50% return to Filmmakers = $75,000</td>
        </tr>
        <tr class="r3">
          <td>Domestic Video on Demand (digital download and rental): Parcelry, Tunebox, Reelio on Demand, Streamkit (using Relaybrook or other</td>
          <td>3 - 6 Months</td>
          <td>6 - 12 Months</td>
          <td>125,000 Downloads at $4. 50% - 60% to Filmmakers= $75,000 - $300,000</td>
        </tr>
        <tr class="r4">
          <td>International theatrical (sold through foreign sales agent at IFX or elsewhere)</td>
          <td>Variable</td>
          <td>6 - 12 Months</td>
          <td>$25,000 (Low End) - $275,000 (High End)</td>
        </tr>
        <tr class="r5">
          <td>International video (initial) (sold through foreign sales agent at IFX or elsewhere)</td>
          <td>9 - 12 Months</td>
          <td>9 - 12 Months</td>
          <td>Video Inc. with Theatrical, assumes All Right Sold and multiple territories</td>
        </tr>
        <tr class="r6">
          <td>Domestic Cable VOD</td>
          <td>12 -15 Months</td>
          <td>18 Months</td>
          <td>--</td>
        </tr>
        <tr class="r7">
          <td>Domestic Subscription-based VOD (Flickstream, LUMO, Cinevault)</td>
          <td>18 - 24 Months</td>
          <td>12 - 36 Months</td>
          <td>--</td>
        </tr>
      </tbody>
    </table>

    <div class="page-number">7</div>
  </section>
</body>
</html>
```